we are a college and require a design of a printable graduation certificate

our courses range from certicate III to Diploma

We would a high quality design, similar to a unveristy degree, so its meaning full to the students and looks great on the wall

our college website is: www.marlowinstitute.example.au

College

• security feature like water mark or stamp

```html
<!DOCTYPE html>
<html lang="en">
<head>
<meta charset="utf-8">
<title>Graduation Certificate</title>
<link rel="stylesheet" href="https://fonts.googleapis.com/css2?family=Alegreya+Sans:wght@400;500&family=Parisienne&family=Tinos&family=Arimo:ital@1&display=swap">
<style>
  :root {
    --paper: #ffffff;
    --navy: #1c3447;
    --navy-deep: #0f2233;
    --gold: #c9b274;
    --gold-light: #efe2b0;
    --gold-dark: #8a7336;
    --silver: #c9d0d6;
    --silver-dark: #8d98a2;
    --ink: #3d3d3d;
    --ink-dark: #111111;
    --script: #8c7c63;
    --tint-rose: #f6dede;
    --tint-cream: #fbf3dc;
    --guilloche: #e6ebf1;
  }
  html, body { margin: 0; padding: 0; overflow: hidden; }
  body { width: 1200px; height: 1000px; background: var(--paper); }
  .canvas { position: relative; width: 1200px; height: 1000px; overflow: hidden; background: var(--paper); }
  .frame-art { position: absolute; left: 0; top: 0; }
  .text { position: absolute; left: 0; width: 1166px; text-align: center; margin: 0; }
  .institute-the { top: 260px; font: 500 38px/1 'Alegreya Sans', sans-serif; color: var(--ink); }
  .institute-name { top: 297px; font: 500 40px/1 'Alegreya Sans', sans-serif; color: var(--ink); }
  .certify-line { top: 339px; font: 400 29px/1 'Alegreya Sans', sans-serif; color: var(--ink-dark); }
  .meta { position: absolute; top: 347px; font: italic 11px/14px 'Arimo', sans-serif; color: var(--ink-dark); margin: 0; }
  .meta-issue { left: 178px; text-align: left; }
  .meta-number { left: 849px; text-align: left; }
  .graduate-name { top: 378px; font: 400 68px/1.2 'Parisienne', cursive; color: var(--script); }
  .intro-line { top: 478px; font: 400 16px/1 'Alegreya Sans', sans-serif; color: var(--ink-dark); }
  .award-title { top: 510px; font: 400 35px/1 'Tinos', serif; color: var(--ink-dark); }
  .award-body { top: 555px; left: 185px; width: 796px; font: 400 15px/28.5px 'Alegreya Sans', sans-serif; color: var(--ink-dark); }
  .signature { position: absolute; top: 749px; width: 271px; border-top: 1px solid var(--ink-dark); text-align: center; font: 400 19px/1 'Tinos', serif; color: var(--ink-dark); padding-top: 9px; }
  .signature-dean { left: 167px; }
  .signature-vice { left: 718px; }
  .seal { position: absolute; left: 531px; top: 724px; width: 104px; height: 104px; }
  .seal-label { position: absolute; left: 531px; top: 761px; width: 104px; text-align: center; font: 500 28px/1 'Alegreya Sans', sans-serif; color: var(--gold-dark); transform: scaleX(0.8); }
</style>
</head>
<body>
<main class="canvas">
  <svg class="frame-art" width="1200" height="1000" viewBox="0 0 1200 1000">
    <defs>
      <linearGradient id="backdropTint" x1="0" y1="0" x2="1" y2="0">
        <stop offset="0" stop-color="var(--tint-rose)" stop-opacity="0.5"/>
        <stop offset="0.5" stop-color="var(--guilloche)" stop-opacity="0.5"/>
        <stop offset="1" stop-color="var(--tint-cream)" stop-opacity="0.6"/>
      </linearGradient>
      <linearGradient id="borderGold" x1="0" y1="0" x2="0" y2="1">
        <stop offset="0" stop-color="var(--gold)"/>
        <stop offset="0.5" stop-color="var(--gold-dark)"/>
        <stop offset="1" stop-color="var(--gold)"/>
      </linearGradient>
      <linearGradient id="chainSilver" x1="0" y1="0" x2="1" y2="1">
        <stop offset="0" stop-color="var(--silver)"/>
        <stop offset="0.5" stop-color="var(--silver-dark)"/>
        <stop offset="1" stop-color="var(--silver)"/>
      </linearGradient>
      <radialGradient id="watermarkGlobe" cx="0.5" cy="0.5" r="0.5">
        <stop offset="0" stop-color="var(--guilloche)" stop-opacity="0.3"/>
        <stop offset="0.8" stop-color="var(--guilloche)" stop-opacity="0.8"/>
        <stop offset="1" stop-color="var(--guilloche)" stop-opacity="0"/>
      </radialGradient>
      <radialGradient id="sealGold" cx="0.4" cy="0.35" r="0.7">
        <stop offset="0" stop-color="var(--gold-light)"/>
        <stop offset="0.6" stop-color="var(--gold)"/>
        <stop offset="1" stop-color="var(--gold-dark)"/>
      </radialGradient>
    </defs>

    <rect class="security-backdrop" x="30" y="135" width="1140" height="785" fill="url(#backdropTint)" role="img" aria-label="Faint wavy guilloche security pattern behind the certificate"/>

    <g class="border-outer" role="img" aria-label="Ornamental navy and gold guilloche border">
      <rect x="55" y="165" width="1090" height="728" fill="url(#borderGold)"/>
      <rect x="70" y="180" width="1060" height="698" fill="var(--navy-deep)"/>
      <rect x="78" y="188" width="1044" height="682" fill="none" stroke="var(--gold)" stroke-width="6" opacity="0.7"/>
    </g>

    <rect class="border-inner-band" x="118" y="212" width="930" height="615" fill="var(--navy)"/>

    <g class="inner-panel">
      <rect x="160" y="265" width="850" height="525" fill="var(--paper)"/>
      <ellipse cx="583" cy="525" rx="425" ry="298" fill="var(--paper)"/>
    </g>

    <circle class="security-watermark" cx="583" cy="600" r="250" fill="url(#watermarkGlobe)" role="img" aria-label="Faint guilloche globe watermark as a security feature"/>

    <rect class="chain-ornament" x="135" y="236" width="896" height="572" rx="10" fill="none" stroke="url(#chainSilver)" stroke-width="20" role="img" aria-label="Silver and gold chain ornament framing the panel"/>
  </svg>

  <p class="text institute-the">The</p>
  <p class="text institute-name">Professional Institute of Diplomas &amp; Certificates</p>
  <p class="text certify-line">This is to certify that</p>

  <p class="meta meta-issue">Given this day<br>January 26, 2012</p>
  <p class="meta meta-number">Certificate number: 002123<br>Expiration Date: Jan 26, 2013</p>

  <p class="text graduate-name">John Parker Doe</p>
  <p class="text intro-line">There are many variations of passages of Lorem Ipsum available</p>
  <p class="text award-title">Highlight Acheivement</p>
  <p class="text award-body">Lorem Ipsum is simply dummy text of the printing and typesetting industry. Lorem Ipsum has been the industry's standard dummy text ever since the 1500s, when an unknown printer took a galley of type and scrambled it to make a type specimen book. It has survived not only five centuries, but also the leap into electronic typesetting, remaining essentially unchanged. It was popularised in the 1960s with the release of Corvell sheets containing Lorem Ipsum passages, and more recently with desktop publishing software like Brindle PageSetter including versions of Lorem Ipsum.</p>

  <div class="signature signature-dean">Dean</div>
  <div class="signature signature-vice">Vice Dean</div>

  <svg class="seal" viewBox="0 0 100 100" aria-hidden="true">
    <polygon fill="url(#sealGold)" points="100,50 91.2,58.2 96.2,69.2 84.9,73.4 85.4,85.4 73.4,84.9 69.2,96.2 58.2,91.2 50,100 41.8,91.2 30.8,96.2 26.6,84.9 14.6,85.4 15.1,73.4 3.8,69.2 8.8,58.2 0,50 8.8,41.8 3.8,30.8 15.1,26.6 14.6,14.6 26.6,15.1 30.8,3.8 41.8,8.8 50,0 58.2,8.8 69.2,3.8 73.4,15.1 85.4,14.6 84.9,26.6 96.2,30.8 91.2,41.8"/>
  </svg>
  <div class="seal-label">SEAL</div>
</main>
</body>
</html>
```